Calvin Pruett Insurance Biz Card
Biz card and stationary
Calvin Pruett Insurance Biz Card - Financial Services
Creative Brief
Professional
Calvin Pruett
Independent Agent
Greensboro, NC
pruettgroup@lanvex.example.net
www.calvinpruettinsurance.example.com
please use the logo we upload, and keep all font at a size 9 or 10.
please use the content we upload for an example of the back of the card

```html
<!DOCTYPE html>
<html lang="en">
<head>
<meta charset="utf-8">
<title>Calvin Pruett Insurance — Business Card and Stationery</title>
<link href="https://fonts.googleapis.com/css2?family=Libre+Baskerville:wght@700&family=Open+Sans:wght@400;600&display=swap" rel="stylesheet">
<style>
  :root {
    --navy: #1f3566;
    --navy-deep: #16284f;
    --grey: #a9aaa4;
    --paper: #ffffff;
    --ink: #333a48;
    --muted: #8a8f99;
    --watermark: #e3e5ec;
    --backdrop: #d9c6a6;
  }
  * { box-sizing: border-box; margin: 0; padding: 0; }
  html, body { width: 1200px; height: 674px; overflow: hidden; }
  body { background: var(--backdrop); font-family: "Open Sans", sans-serif; color: var(--ink); position: relative; }
  .piece { position: absolute; background: var(--paper); overflow: hidden; box-shadow: 0 2px 6px rgba(60,40,10,.35); }
  .label { position: absolute; font-size: 7px; color: #3b2a14; text-align: center; font-weight: 600; }
  .curve { position: absolute; inset: 0; width: 100%; height: 100%; }
  .brand { position: absolute; display: flex; align-items: center; gap: 5px; }
  .brand-mark { background: var(--navy); flex: none; }
  .brand-name { font-family: "Libre Baskerville", serif; font-weight: 700; color: var(--navy); line-height: 1.05; }
  .brand.light .brand-mark { background: var(--paper); }
  .brand.light .brand-name { color: var(--paper); }
  .small { position: absolute; font-size: 4.6px; line-height: 1.45; color: var(--ink); }
  .small.light { color: var(--paper); }
  .watermark { position: absolute; background: var(--watermark); }
  .fax-title { position: absolute; right: 34px; top: 66px; font-size: 8px; font-weight: 600; letter-spacing: 1px; }
  .fax-table { position: absolute; left: 16px; right: 16px; top: 78px; border-collapse: collapse; font-size: 5px; }
  .fax-table td { border: .6px solid #777; height: 13px; padding: 0 3px; width: 25%; }
  .fax-checks { position: absolute; left: 16px; top: 146px; display: flex; gap: 14px; font-size: 4.6px; }
  .fax-checks span::before { content: ""; display: inline-block; width: 5px; height: 5px; border: .6px solid #555; margin-right: 3px; vertical-align: -1px; }
  .flap { position: absolute; left: 0; top: 0; width: 100%; height: 100%; }
</style>
</head>
<body>

<!-- Business card front -->
<div class="label" style="left:110px;top:18px;width:139px">Business Card (Front)</div>
<div class="piece card-front" style="left:110px;top:29px;width:139px;height:80px">
  <svg class="curve" viewBox="0 0 139 80" preserveAspectRatio="none"><path d="M0 0H10Q4 40 10 80H0Z" fill="var(--navy)"/><path d="M139 0V80H130Q136 40 130 0Z" fill="var(--navy)"/></svg>
  <div class="brand" style="left:24px;top:28px"><div class="brand-mark" style="width:20px;height:20px"></div><div class="brand-name" style="font-size:8px">Calvin Pruett<br>Insurance</div></div>
</div>

<!-- Business card back option 1 -->
<div class="label" style="left:271px;top:18px;width:139px">Business Card (Back) Option 1</div>
<div class="piece" style="left:271px;top:29px;width:139px;height:80px">
  <div class="brand" style="left:52px;top:10px"><div class="brand-mark" style="width:10px;height:10px"></div><div class="brand-name" style="font-size:4.6px">Calvin Pruett<br>Insurance</div></div>
  <div class="small" style="left:0;right:0;top:32px;text-align:center"><b>Calvin Pruett</b><br>Independent Agent<br>1420 Lindale Court, Greensboro, NC<br>P (336) 555-0142 · F (336) 555-0143<br>pruettgroup@lanvex.example.net<br>www.calvinpruettinsurance.example.com</div>
</div>

<!-- Business card back option 2 -->
<div class="label" style="left:439px;top:18px;width:137px">Business Card (Back) Option 2</div>
<div class="piece" style="left:439px;top:29px;width:137px;height:80px;background:var(--grey)">
  <div class="small light" style="left:0;right:0;top:22px;text-align:center"><b>Calvin Pruett</b><br>Independent Agent<br>1420 Lindale Court, Greensboro, NC<br>P (336) 555-0142 · F (336) 555-0143<br>pruettgroup@lanvex.example.net<br>www.calvinpruettinsurance.example.com</div>
</div>

<!-- Business card back option 3 -->
<div class="label" style="left:600px;top:18px;width:134px">Business Card (Back) Option 3</div>
<div class="piece" style="left:600px;top:29px;width:134px;height:80px;background:var(--navy)">
  <div class="brand light" style="left:46px;top:8px"><div class="brand-mark" style="width:10px;height:10px"></div><div class="brand-name" style="font-size:4.6px">Calvin Pruett<br>Insurance</div></div>
  <div class="small light" style="left:0;right:0;top:30px;text-align:center"><b>Calvin Pruett</b><br>Independent Agent<br>1420 Lindale Court, Greensboro, NC<br>P (336) 555-0142 · F (336) 555-0143<br>pruettgroup@lanvex.example.net<br>www.calvinpruettinsurance.example.com</div>
</div>

<!-- Envelope front -->
<div class="label" style="left:763px;top:18px;width:406px">Envelope (Front)</div>
<div class="piece" style="left:763px;top:29px;width:406px;height:211px">
  <svg class="curve" viewBox="0 0 406 211" preserveAspectRatio="none"><path d="M0 0H14Q4 105 14 211H0Z" fill="var(--navy)"/><path d="M406 0V211H392Q402 105 392 0Z" fill="var(--navy)"/></svg>
  <div class="brand" style="left:26px;top:16px"><div class="brand-mark" style="width:24px;height:24px"></div><div class="brand-name" style="font-size:9px">Calvin Pruett<br>Insurance</div></div>
  <div class="small" style="left:58px;top:46px">1420 Lindale Court<br>Greensboro, NC 27408</div>
</div>

<!-- Fax cover -->
<div class="label" style="left:29px;top:138px;width:355px">Fax Cover</div>
<div class="piece fax-cover" style="left:29px;top:149px;width:355px;height:504px">
  <svg class="curve" viewBox="0 0 355 504" preserveAspectRatio="none"><path d="M0 0H12Q2 30 0 70Z" fill="var(--navy)"/><path d="M355 0V70Q352 30 340 0Z" fill="var(--navy)"/><path d="M0 504V380Q4 470 40 504Z" fill="var(--navy)"/><path d="M355 504H315Q351 470 355 380Z" fill="var(--navy)"/></svg>
  <div class="brand" style="left:16px;top:16px"><div class="brand-mark" style="width:22px;height:22px"></div><div class="brand-name" style="font-size:8.5px">Calvin Pruett<br>Insurance</div></div>
  <div class="small" style="left:230px;top:16px">Greensboro, NC<br>P (336) 555-0142<br>F (336) 555-0143<br>pruettgroup@lanvex.example.net</div>
  <div class="fax-title">FAX</div>
  <table class="fax-table">
    <tr><td>To:</td><td></td><td>From:</td><td></td></tr>
    <tr><td>Fax:</td><td></td><td>Pages:</td><td></td></tr>
    <tr><td>Phone:</td><td></td><td>Date:</td><td></td></tr>
    <tr><td>Re:</td><td></td><td>CC:</td><td></td></tr>
  </table>
  <div class="fax-checks"><span>Urgent</span><span>For Review</span><span>Please Comment</span><span>Please Reply</span><span>Please Recycle</span></div>
  <div class="watermark" style="left:90px;top:200px;width:150px;height:150px"></div>
</div>

<!-- Letterhead -->
<div class="label" style="left:398px;top:138px;width:351px">Letterhead</div>
<div class="piece letterhead" style="left:398px;top:149px;width:351px;height:504px">
  <svg class="curve" viewBox="0 0 351 504" preserveAspectRatio="none"><path d="M0 0H12Q2 30 0 70Z" fill="var(--navy)"/><path d="M351 0V70Q348 30 336 0Z" fill="var(--navy)"/><path d="M0 504V380Q4 470 40 504Z" fill="var(--navy)"/><path d="M351 504H311Q347 470 351 380Z" fill="var(--navy)"/></svg>
  <div class="brand" style="left:16px;top:16px"><div class="brand-mark" style="width:22px;height:22px"></div><div class="brand-name" style="font-size:8.5px">Calvin Pruett<br>Insurance</div></div>
  <div class="small" style="left:228px;top:16px">Greensboro, NC<br>P (336) 555-0142<br>F (336) 555-0143<br>pruettgroup@lanvex.example.net</div>
  <div class="watermark" style="left:98px;top:180px;width:150px;height:150px"></div>
</div>

<!-- Envelope back option 1 -->
<div class="label" style="left:763px;top:302px;width:406px">Envelope (Back) Option 1</div>
<div class="piece" style="left:763px;top:312px;width:406px;height:96px">
  <svg class="flap" viewBox="0 0 406 96" preserveAspectRatio="none"><path d="M0 0H406L230 60Q203 72 176 60Z" fill="var(--paper)" stroke="#b9bcc4" stroke-width="1"/></svg>
  <div class="brand" style="left:168px;top:20px"><div class="brand-mark" style="width:16px;height:16px"></div><div class="brand-name" style="font-size:7px">Calvin Pruett<br>Insurance</div></div>
</div>

<!-- Envelope back option 2 -->
<div class="label" style="left:763px;top:417px;width:406px">Envelope (Back) Option 2</div>
<div class="piece" style="left:763px;top:427px;width:406px;height:106px">
  <svg class="flap" viewBox="0 0 406 106" preserveAspectRatio="none"><path d="M0 0H406L230 68Q203 80 176 68Z" fill="var(--grey)"/></svg>
  <div class="brand light" style="left:168px;top:22px"><div class="brand-mark" style="width:16px;height:16px"></div><div class="brand-name" style="font-size:7px">Calvin Pruett<br>Insurance</div></div>
</div>

<!-- Envelope back option 3 -->
<div class="label" style="left:763px;top:530px;width:406px">Envelope (Back) Option 3</div>
<div class="piece" style="left:763px;top:540px;width:406px;height:103px">
  <svg class="flap" viewBox="0 0 406 103" preserveAspectRatio="none"><path d="M0 0H406L230 66Q203 78 176 66Z" fill="var(--navy)"/></svg>
  <div class="brand light" style="left:168px;top:20px"><div class="brand-mark" style="width:16px;height:16px"></div><div class="brand-name" style="font-size:7px">Calvin Pruett<br>Insurance</div></div>
</div>

</body>
</html>
```